Letterhead for financial advisor-insurance agent firm

Our company, Harlow Pemberton Insurance & Investments, is an insurance (health, life, home, auto, etc) and investment brokerage offering a suite of options to meet client needs. We need letterhead that is professional and embodies strength, security and sophistication.

http://jobs.brieftrove.example/job.aspx?id=518264

Industry/Entity Type

Investment

```html
<!DOCTYPE html>
<html lang="en">
<head>
<meta charset="utf-8">
<title>Harlow Pemberton Insurance &amp; Investments – Stationery</title>
<link href="https://fonts.googleapis.com/css2?family=Cinzel:wght@500&family=Open+Sans:wght@400;700&display=swap" rel="stylesheet">
<style>
  :root {
    --navy: #2b3252;
    --slate: #5d6a73;
    --paper: #ffffff;
    --stage: #ffffff;
    --rule: #c9c9cc;
    --ghost: #535d78;
    --ink-light: #ffffff;
  }
  * { box-sizing: border-box; margin: 0; padding: 0; }
  html, body { width: 1200px; height: 900px; overflow: hidden; background: var(--stage); }
  body { position: relative; font-family: "Open Sans", Arial, sans-serif; }

  .letterhead {
    position: absolute; left: 58px; top: 25px; width: 592px; height: 840px;
    background: var(--paper); border: 1px solid var(--rule);
  }
  .wordmark { text-align: center; font-family: "Cinzel", "Times New Roman", serif; font-weight: 500; color: var(--navy); }
  .letterhead .wordmark { position: absolute; top: 98px; left: 0; right: 0; }
  .wordmark-name { display: block; font-size: 27px; letter-spacing: 0.5px; line-height: 1.1; }
  .wordmark-tag { display: block; font-size: 11px; letter-spacing: 1px; margin-top: 2px; }

  .footer-band {
    position: absolute; left: 0; bottom: 14px; width: 100%; height: 77px;
  }
  .footer-band .band { position: absolute; left: 0; top: 0; width: 492px; height: 100%; background: var(--navy); }
  .footer-band .block { position: absolute; left: 497px; top: 0; width: 72px; height: 100%; background: var(--navy); }
  .footer-band .strip { position: absolute; left: 574px; top: 0; width: 18px; height: 100%; background: var(--navy); }

  .contact {
    position: absolute; display: grid; grid-template-columns: auto auto; column-gap: 34px; row-gap: 2px;
    color: var(--ink-light); font-size: 11px; line-height: 15px;
  }
  .footer-band .contact { left: 20px; top: 19px; }
  .contact li { list-style: none; display: flex; align-items: center; gap: 6px; white-space: nowrap; }
  .contact svg { width: 10px; height: 10px; flex: none; fill: var(--ink-light); }

  .card { position: absolute; width: 400px; height: 230px; border: 1px solid var(--rule); overflow: hidden; }
  .card-front { left: 740px; top: 300px; background: var(--paper); }
  .card-front .wordmark { position: absolute; top: 46px; left: 40px; right: 0; }
  .card-front .wordmark-name { font-size: 22px; }
  .card-front .wordmark-tag { font-size: 9px; }
  .holder { position: absolute; left: 18px; top: 104px; color: var(--navy); }
  .holder-name { font-weight: 700; font-size: 12px; letter-spacing: 0.2px; display: block; }
  .holder-role { font-size: 8px; font-weight: 700; display: block; }
  .card-front .band { position: absolute; left: 0; top: 140px; width: 300px; height: 76px; background: var(--navy); }
  .card-front .block { position: absolute; left: 305px; top: 140px; width: 60px; height: 76px; background: var(--navy); }
  .card-front .strip { position: absolute; left: 370px; top: 140px; width: 14px; height: 76px; background: var(--navy); }
  .card-front .contact { left: 12px; top: 153px; font-size: 9px; line-height: 13px; column-gap: 30px; }
  .card-front .contact svg { width: 8px; height: 8px; }

  .card-back { left: 740px; top: 570px; background: var(--navy); border-color: var(--navy); }
  .card-back .wordmark { position: absolute; top: 92px; left: 0; right: 0; color: var(--ghost); }
  .card-back .wordmark-name { font-size: 24px; }
  .card-back .wordmark-tag { font-size: 10px; }
</style>
</head>
<body>

<svg width="0" height="0" style="position:absolute" aria-hidden="true">
  <symbol id="icon-phone" viewBox="0 0 10 10"><rect x="0" y="0" width="10" height="10" rx="1.5"/><rect x="2.5" y="2" width="5" height="6" rx="1" fill="#2b3252"/></symbol>
  <symbol id="icon-mobile" viewBox="0 0 10 10"><path d="M2 1 L4 1 L4.8 3 L3.6 4 Q4.6 6 6.2 6.6 L7 5.4 L9 6.2 L9 8 Q6 9.5 3 6.5 Q0.5 4 2 1 Z"/></symbol>
  <symbol id="icon-fax" viewBox="0 0 10 10"><rect x="0" y="0" width="10" height="10" rx="1.5"/><rect x="2" y="4" width="6" height="3.5" fill="#2b3252"/></symbol>
  <symbol id="icon-mail" viewBox="0 0 10 10"><rect x="0" y="1.5" width="10" height="7" rx="1"/><path d="M1 2.5 L5 5.5 L9 2.5" stroke="#2b3252" stroke-width="1" fill="none"/></symbol>
  <symbol id="icon-web" viewBox="0 0 10 10"><circle cx="5" cy="5" r="5"/><path d="M0.5 5 H9.5 M5 0.5 V9.5 M2 2.5 Q5 4 8 2.5 M2 7.5 Q5 6 8 7.5" stroke="#2b3252" stroke-width="0.8" fill="none"/></symbol>
  <symbol id="icon-pin" viewBox="0 0 10 10"><rect x="0" y="0" width="10" height="10" rx="1.5"/><path d="M5 1.8 A2.2 2.2 0 0 1 7.2 4 Q7.2 5.5 5 8.2 Q2.8 5.5 2.8 4 A2.2 2.2 0 0 1 5 1.8 Z" fill="#2b3252"/></symbol>
</svg>

<section class="letterhead" aria-label="Letterhead">
  <header class="wordmark">
    <span class="wordmark-name">Harlow Pemberton</span>
    <span class="wordmark-tag">Insurance &amp; Investments</span>
  </header>

  <footer class="footer-band">
    <div class="band"></div>
    <div class="block"></div>
    <div class="strip"></div>
    <ul class="contact">
      <li><svg><use href="#icon-phone"/></svg>0142 318 760</li>
      <li><svg><use href="#icon-mail"/></svg>harlow@harlowpemberton.example</li>
      <li><svg><use href="#icon-mobile"/></svg>0961 275 430</li>
      <li><svg><use href="#icon-web"/></svg>www.harlowpemberton.example</li>
      <li><svg><use href="#icon-fax"/></svg>0961 275 431</li>
      <li><svg><use href="#icon-pin"/></svg>1180 Larkfield Avenue, Easton</li>
    </ul>
  </footer>
</section>

<section class="card card-front" aria-label="Business card, front">
  <div class="wordmark">
    <span class="wordmark-name">Harlow Pemberton</span>
    <span class="wordmark-tag">Insurance &amp; Investments</span>
  </div>
  <div class="holder">
    <span class="holder-name">HARLOW PEMBERTON</span>
    <span class="holder-role">Director</span>
  </div>
  <div class="band"></div>
  <div class="block"></div>
  <div class="strip"></div>
  <ul class="contact">
    <li><svg><use href="#icon-phone"/></svg>0142 318 760</li>
    <li><svg><use href="#icon-mail"/></svg>harlow@harlowpemberton.example</li>
    <li><svg><use href="#icon-mobile"/></svg>0961 275 430</li>
    <li><svg><use href="#icon-web"/></svg>www.harlowpemberton.example</li>
    <li><svg><use href="#icon-fax"/></svg>0961 275 431</li>
    <li><svg><use href="#icon-pin"/></svg>1180 Larkfield Avenue, Easton</li>
  </ul>
</section>

<section class="card card-back" aria-label="Business card, back">
  <div class="wordmark">
    <span class="wordmark-name">Harlow Pemberton</span>
    <span class="wordmark-tag">Insurance &amp; Investments</span>
  </div>
</section>

</body>
</html>
```